Brightwater Systems Website

I am starting an IT consulting business called Brightwater Systems. I recently completed a logo contest on ArtHive and am now looking to put together a basic website. I can provide text and content but am looking for a site design with layout and graphics. I am attaching my logo below. I was thinking of a dark blue and white theme for the website (similar to the logo). However, I am open to ideas. Graphics can be a mix of business and high tech as that is the image I am trying to convey. The site will be relatively simple and probably have only 3 - 5 pages (Home, About Us, Services, Contact, etc.)
Target Market(s)
United States commercial companies and government contractors
Industry/Entity Type
Consulting
Coding
Coded - Design and coding required
Number of Pages Required
4 page
Look and feel

```html
<!DOCTYPE html>
<html lang="en">
<head>
<meta charset="utf-8">
<title>Brightwater Systems – About Us</title>
<link href="https://fonts.googleapis.com/css2?family=Oswald:wght@400;500&family=Arimo:wght@400;700&family=Montserrat:wght@300;400&display=swap" rel="stylesheet">
<style>
:root{
  --navy:#1c2233;
  --band:#0b4d9e;
  --blue:#1a74c9;
  --blue-bright:#2486dc;
  --ink:#2b2f3a;
  --muted:#555b66;
  --footer:#262c46;
  --mist:#e8f2f7;
  --white:#ffffff;
}
*{margin:0;padding:0;box-sizing:border-box}
html,body{width:1200px;height:3968px;overflow:hidden}
body{position:relative;background:var(--white);font-family:"Arimo",Arial,sans-serif;color:var(--ink)}
.abs{position:absolute}
.head{font-family:"Oswald",sans-serif;font-weight:500;text-transform:uppercase;letter-spacing:.2px}
.txt{font-size:11.5px;line-height:17px;color:var(--muted)}
.center{text-align:center}

/* header */
.site-header{position:absolute;left:0;top:0;width:1200px;height:80px;background:var(--white)}
.brand{position:absolute;display:flex;align-items:center;gap:8px;font-family:"Oswald",sans-serif;font-weight:500;font-size:22px;letter-spacing:1.5px;color:var(--navy);text-transform:uppercase}
.brand .dot{width:14px;height:14px;border-radius:50%;background:var(--blue)}
.nav a{position:absolute;top:30px;transform:translateX(-50%);font-family:"Oswald",sans-serif;font-size:13px;color:var(--navy);text-decoration:none;white-space:nowrap}
.nav a.active{color:var(--navy)}
.nav a.active::after{content:"";position:absolute;left:-8px;right:-8px;top:47px;height:3px;background:var(--blue)}

/* hero */
.hero{position:absolute;left:0;top:80px;width:1200px;height:390px;background:linear-gradient(100deg,#0e1d3c 0%,#1a3563 45%,#0c1a36 100%)}
.hero h1{position:absolute;width:1200px;text-align:center;font-family:"Montserrat",sans-serif;font-weight:300;color:var(--white)}

/* about */
.kicker{font-family:"Oswald",sans-serif;font-size:15px;color:var(--blue);text-transform:uppercase}
.bar{position:absolute;height:4px;background:var(--blue)}
.btn{position:absolute;height:37px;border-radius:19px;font-family:"Oswald",sans-serif;font-size:13px;display:flex;align-items:center;justify-content:center;text-transform:uppercase}
.btn-outline{border:2px solid var(--blue);color:var(--blue)}
.btn-solid{background:var(--band);color:var(--white)}
.photo{position:absolute;border-radius:50%}
.faint{position:absolute;background:#c9d4e2;opacity:.35}

/* numbers */
.band{position:absolute;left:0;width:1200px}
.stat{position:absolute;width:150px;height:150px;border:2px solid rgba(255,255,255,.85);border-radius:50%;color:var(--white);text-align:center}
.stat::before{content:"";position:absolute;left:69px;top:-6px;width:9px;height:9px;border-radius:50%;border:2px solid #fff;background:var(--band)}
.stat b{display:block;font-family:"Oswald",sans-serif;font-weight:500;font-size:34px;margin-top:42px;line-height:40px}
.stat span{font-family:"Oswald",sans-serif;font-size:10px;text-transform:uppercase}

/* team */
.member{position:absolute;width:210px;text-align:center}
.member h3{font-family:"Oswald",sans-serif;font-weight:400;font-size:16px;color:var(--blue);margin-bottom:6px}

/* why */
.step{position:absolute;width:280px;text-align:center;color:var(--white)}
.step h3{font-family:"Oswald",sans-serif;font-weight:500;font-size:16px;text-transform:uppercase;margin-bottom:6px}
.step p{font-size:11px;line-height:15px}

/* contact */
.field-label{position:absolute;font-family:"Oswald",sans-serif;font-size:12px;color:var(--navy);text-transform:uppercase}
.field-value{position:absolute;font-size:10.5px;color:#8a8f99}
.field-line{position:absolute;height:1px;background:#d5d9df}
.info-label{font-family:"Oswald",sans-serif;font-size:12px;color:var(--white);text-transform:uppercase;margin-bottom:4px}
.info-text{font-size:11px;line-height:14px;color:#e6eefa;margin-bottom:22px}

/* footer */
.fnav a{position:absolute;top:3868px;transform:translateX(-50%);font-family:"Oswald",sans-serif;font-size:14px;color:var(--white);text-decoration:none;white-space:nowrap}
.fnav a.active{color:var(--blue-bright)}
</style>
</head>
<body>

<header class="site-header">
  <div class="brand" style="left:142px;top:22px"><span class="dot"></span>Brightwater Systems</div>
  <nav class="nav">
    <a style="left:554px">HOME</a>
    <a class="active" style="left:661px">ABOUT US</a>
    <a style="left:789px">OUR SERVICES</a>
    <a style="left:905px">BLOG</a>
    <a style="left:1016px">CONTACT US</a>
  </nav>
</header>

<section class="hero" role="img" aria-label="Dark blue photo of a businessman in a suit at a meeting">
  <h1 style="top:164px;font-size:23px">ABOUT US</h1>
  <h1 style="top:200px;font-size:26px">YOUR BUSINESS A GROWTH</h1>
</section>

<!-- about -->
<section class="about">
  <div class="abs kicker" style="left:134px;top:556px">About our company</div>
  <div class="abs head" style="left:134px;top:582px;font-size:28px;color:var(--navy)">World’s Premier</div>
  <div class="abs head" style="left:134px;top:620px;font-size:28px;color:var(--navy)"><span style="color:var(--blue)">Business</span> &amp; <span style="color:var(--blue)">Technology</span> Organization</div>
  <div class="bar" style="left:134px;top:671px;width:77px"></div>
  <p class="abs txt" style="left:134px;top:696px;width:462px">It uses a dictionary of over 200 Latin words, combined with a handful of model sentence structures, to generate Lorem Ipsum which looks reasonable. The generated Lorem Ipsum is therefore always free from repetition, injected humour, or non-characteristic words etc. It uses a dictionary of over 200 Latin words, combined with a handful of model sentence structures, to generate Lorem Ipsum which looks reasonable.</p>
  <div class="btn btn-outline" style="left:135px;top:804px;width:150px">Download Profile</div>
  <div class="btn btn-solid" style="left:293px;top:804px;width:120px">Get in touch</div>

  <div class="faint" role="img" aria-label="Dotted grid decoration" style="left:990px;top:500px;width:73px;height:70px;opacity:.25"></div>
  <div class="faint" role="img" aria-label="Dotted triangle decoration" style="left:54px;top:870px;width:65px;height:54px;clip-path:polygon(0 0,100% 0,50% 100%)"></div>

  <div class="photo" role="img" aria-label="Photo of a team of colleagues gathered around a desk" style="left:795px;top:513px;width:268px;height:268px;background:linear-gradient(135deg,#c9d6e6,#7c93b3)"></div>
  <svg class="abs" style="left:842px;top:712px" width="240" height="240" viewBox="0 0 240 240" aria-hidden="true">
    <circle cx="120" cy="120" r="110" fill="none" stroke="#1a74c9" stroke-width="8" stroke-dasharray="440 251" transform="rotate(-20 120 120)"/>
    <circle cx="120" cy="120" r="95" fill="none" stroke="#1c2233" stroke-width="9" stroke-dasharray="200 397" transform="rotate(-100 120 120)"/>
    <circle cx="120" cy="120" r="82" fill="none" stroke="#1a74c9" stroke-width="3" stroke-dasharray="260 255" transform="rotate(60 120 120)"/>
    <circle cx="120" cy="120" r="42" fill="#2a2f45"/>
  </svg>
  <div class="photo" role="img" aria-label="Photo of a smiling woman working on a laptop" style="left:670px;top:670px;width:230px;height:230px;background:linear-gradient(135deg,#e4e6ea,#9aa3ae);border:5px solid #fff"></div>
</section>

<!-- numbers -->
<section class="band" style="top:967px;height:404px;background:var(--band)">
  <div class="abs head" style="left:134px;top:88px;font-size:15px;font-weight:400;color:#fff">Global Experience</div>
  <div class="abs head" style="left:134px;top:114px;font-size:28px;color:#fff">Brightwater in Numbers</div>
  <div class="bar" style="left:134px;top:163px;width:55px;background:#fff"></div>
  <p class="abs" style="left:134px;top:190px;width:380px;font-size:12.5px;line-height:19px;color:#fff">It uses a dictionary of over 200 Latin words, combined with a handful of model sentence structures, to generate Lorem Ipsum which looks reasonable. The generated Lorem Ipsum is therefore always free from repetition, injected humour, or non-characteristic words etc. The generated Lorem Ipsum is therefore always free from repetition, injected humour, or non-characteristic words etc.</p>
  <div class="stat" style="left:561px;top:153px"><b>23+</b><span>Years in business</span></div>
  <div class="stat" style="left:738px;top:153px"><b>500+</b><span>Experts &amp; Employees</span></div>
  <div class="stat" style="left:914px;top:153px"><b>10K+</b><span>Satisfied customers</span></div>
</section>

<!-- team -->
<section class="team">
  <div class="abs kicker center" style="left:0;width:1200px;top:1444px;font-size:15px">Professionals</div>
  <div class="abs head center" style="left:0;width:1200px;top:1468px;font-size:28px;color:var(--navy)">Our Management Team</div>
  <div class="bar" style="left:572px;top:1516px;width:56px"></div>

  <svg class="abs" style="left:0;top:1560px" width="1200" height="240" aria-hidden="true">
    <g id="ring">
      <circle cx="237" cy="116" r="96" fill="none" stroke="#1a74c9" stroke-width="9" stroke-dasharray="380 223" transform="rotate(80 237 116)"/>
      <circle cx="237" cy="116" r="96" fill="none" stroke="#1c2233" stroke-width="9" stroke-dasharray="170 433" transform="rotate(-120 237 116)"/>
      <circle cx="237" cy="116" r="82" fill="none" stroke="#1c2233" stroke-width="4" stroke-dasharray="300 215" transform="rotate(200 237 116)"/>
      <circle cx="237" cy="116" r="82" fill="none" stroke="#1a74c9" stroke-width="4" stroke-dasharray="200 315" transform="rotate(20 237 116)"/>
    </g>
    <use href="#ring" x="242"/>
    <use href="#ring" x="484"/>
    <use href="#ring" x="724"/>
  </svg>
  <div class="photo" role="img" aria-label="Portrait photo of a woman" style="left:169px;top:1608px;width:136px;height:136px;background:linear-gradient(135deg,#b8a393,#5a4a42)"></div>
  <div class="photo" role="img" aria-label="Portrait photo of a man with glasses" style="left:411px;top:1608px;width:136px;height:136px;background:linear-gradient(135deg,#d0d0d0,#8b8b8b)"></div>
  <div class="photo" role="img" aria-label="Portrait photo of a bearded man with glasses" style="left:653px;top:1608px;width:136px;height:136px;background:linear-gradient(135deg,#c9cccf,#7c8086)"></div>
  <div class="photo" role="img" aria-label="Portrait photo of a smiling bearded man" style="left:893px;top:1608px;width:136px;height:136px;background:linear-gradient(135deg,#d5d8dc,#8f8a86)"></div>

  <div class="member" style="left:132px;top:1807px"><h3>JOHN DOE</h3><p class="txt">It uses a dictionary of over 200 Latin words, combined with a handful of model sentence structures, to generate Lorem which looks reasonable.</p></div>
  <div class="member" style="left:374px;top:1807px"><h3>JOHN DOE</h3><p class="txt">It uses a dictionary of over 200 Latin word with a handful of model sentence structures,</p></div>
  <div class="member" style="left:616px;top:1807px"><h3>JOHN DOE</h3><p class="txt">It uses a dictionary of over 200 Latin words, combined with a handful of model suctures, sonable.</p></div>
  <div class="member" style="left:856px;top:1807px"><h3>JOHN DOE</h3><p class="txt">Latin words, combined with a handful of model sentence structures, to generate Lorem Ipsum which looks reasonable.</p></div>
</section>

<!-- why choose -->
<section class="band" style="top:1968px;height:451px;background:linear-gradient(180deg,#0c55ad,#0a4b9a)">
  <div class="abs head center" style="left:0;width:1200px;top:72px;font-size:14px;font-weight:400;color:#fff">Why choose us</div>
  <div class="abs head center" style="left:0;width:1200px;top:98px;font-size:28px;color:#fff">All Business and Techh Services</div>
  <div class="bar" style="left:572px;top:146px;width:56px;background:#fff"></div>
  <svg class="abs" style="left:0;top:0" width="1200" height="451" aria-hidden="true">
    <g fill="none" stroke="#fff" stroke-width="2" stroke-dasharray="6 5">
      <path d="M582 157 V205 Q582 216 571 216 H302 Q291 216 291 227 V284"/>
      <path d="M600 157 V284"/>
      <path d="M619 157 V205 Q619 216 630 216 H899 Q910 216 910 227 V284"/>
    </g>
    <g fill="#fff"><circle cx="291" cy="290" r="7"/><circle cx="600" cy="290" r="7"/><circle cx="910" cy="290" r="7"/></g>
    <g font-family="Oswald,sans-serif" font-size="72" fill="none" stroke="#3b84d6" stroke-width="1.5">
      <text x="238" y="300">1</text><text x="541" y="300">2</text><text x="856" y="300">3</text>
    </g>
  </svg>
  <div class="step" style="left:151px;top:318px"><h3>Proven Track Record</h3><p>We There are many variations of passages of Lorem Ipsum available, but the majority have suffered alteration in some form, by injected humour,</p></div>
  <div class="step" style="left:460px;top:318px"><h3>Pioneers in the Industry</h3><p>We There are many variations of passages of Lorem Ipsum available, but the majority have suffered alteration in some form, by injected humour,</p></div>
  <div class="step" style="left:770px;top:318px"><h3>Ensured Service Levels</h3><p>We There are many variations of passages of Lorem Ipsum available, but the majority have suffered alteration in some form, by injected humour,</p></div>
</section>

<!-- mission -->
<section class="band" role="img" aria-label="Dark photo of two businessmen shaking hands" style="top:2419px;height:465px;background:linear-gradient(120deg,#05080f 0%,#162645 50%,#0a0f1c 100%)">
  <div class="abs" style="left:418px;top:45px;width:364px;height:364px;border-radius:50%;border:1px solid rgba(255,255,255,.7)"></div>
  <div class="abs center" style="left:426px;top:53px;width:348px;height:348px;border-radius:50%;background:#eef4fa;border:2px solid var(--blue)">
    <div class="head" style="margin-top:86px;font-size:20px;color:var(--navy)">Our Mission</div>
    <div style="width:56px;height:4px;background:var(--blue);margin:10px auto 22px"></div>
    <p class="txt" style="width:284px;margin:0 auto">We There are many variations of passages of Lorem Ipsum available, but the majority have suffered alteration in some form, by injected humour. We There are many variations of passages of Lorem Ipsum available, but the majority have suffered alteration in some form, by injected humour,</p>
    <svg style="margin-top:20px" width="36" height="36" viewBox="0 0 36 36" aria-hidden="true"><circle cx="18" cy="18" r="16" fill="none" stroke="#1a74c9" stroke-width="2"/><path d="M11 18H25M20 13l5 5-5 5" fill="none" stroke="#1a74c9" stroke-width="2"/></svg>
  </div>
</section>

<!-- contact -->
<section class="band" style="top:2884px;height:666px;background:var(--mist)">
  <div class="faint" role="img" aria-label="Dotted grid decoration" style="left:978px;top:50px;width:146px;height:154px;opacity:.3"></div>
  <div class="faint" role="img" aria-label="Dotted triangle decoration" style="left:46px;top:519px;width:66px;height:54px;clip-path:polygon(0 0,100% 0,50% 100%)"></div>

  <div class="abs" style="left:135px;top:74px;width:199px;height:384px;background:var(--band);padding:80px 22px 0">
    <div class="info-label">Address</div><div class="info-text">Location Town, City name Country</div>
    <div class="info-label">Phone</div><div class="info-text">123-456-7895</div>
    <div class="info-label">Email</div><div class="info-text">info@brightwatersys.com</div>
    <div class="info-label" style="margin-top:54px">Follow us</div>
    <div style="display:flex;gap:14px;margin-top:10px">
      <span style="width:10px;height:10px;border-radius:50%;background:#fff"></span>
      <span style="width:10px;height:10px;border-radius:50%;background:#fff"></span>
      <span style="width:10px;height:10px;border-radius:50%;background:#fff"></span>
      <span style="width:10px;height:10px;border-radius:50%;background:#fff"></span>
    </div>
  </div>
  <div class="abs" role="img" aria-label="Street map showing the office location" style="left:334px;top:74px;width:190px;height:384px;background:linear-gradient(160deg,#eef0e6,#e1e6d4 60%,#d6dfd0)"></div>

  <div class="abs" style="left:487px;top:139px;width:577px;height:453px;background:#fff;box-shadow:0 6px 24px rgba(20,40,80,.12)"></div>
  <div class="abs" style="left:505px;top:158px;width:539px;height:411px;border:2px solid var(--blue)"></div>
  <div class="abs kicker" style="left:524px;top:198px;font-size:14px">Contact us</div>
  <div class="abs head" style="left:524px;top:222px;font-size:27px;color:var(--navy)">Get in touch with us</div>
  <div class="bar" style="left:524px;top:268px;width:55px"></div>

  <div class="field-label" style="left:524px;top:309px">First Name</div>
  <div class="field-line" style="left:524px;top:356px;width:240px"></div>
  <div class="field-label" style="left:787px;top:309px">Lastt Name</div>
  <div class="field-value" style="left:787px;top:336px">Doe</div>
  <div class="field-line" style="left:787px;top:356px;width:240px"></div>

  <div class="field-label" style="left:524px;top:388px">Email Address</div>
  <div class="field-value" style="left:524px;top:415px">johndoe@clientemailid.com</div>
  <div class="field-line" style="left:524px;top:435px;width:240px"></div>
  <div class="field-label" style="left:787px;top:388px">Phone No.</div>
  <div class="field-value" style="left:787px;top:415px">123-456-7895</div>
  <div class="field-line" style="left:787px;top:435px;width:240px"></div>

  <div class="field-label" style="left:524px;top:467px">Message</div>
  <div class="field-value" style="left:524px;top:495px">Let's talk</div>
  <div class="field-line" style="left:524px;top:541px;width:450px"></div>
  <svg class="abs" style="left:986px;top:521px" width="40" height="40" viewBox="0 0 40 40" aria-hidden="true"><circle cx="20" cy="20" r="20" fill="#0b4d9e"/><path d="M12 19l16-7-6 16-3-6z" fill="#fff"/></svg>
</section>

<!-- footer -->
<footer class="band" style="top:3550px;height:418px;background:var(--footer)">
  <div class="abs head center" style="left:0;width:1200px;top:70px;font-size:28px;color:#fff">Our News Letter</div>
  <div class="abs" style="left:340px;top:126px;width:520px;height:42px;border-radius:21px;background:#fff"></div>
  <div class="abs" style="left:370px;top:140px;font-size:11px;color:#8a8f99">johndoe@clientemailid.com</div>
  <div class="abs head" style="left:739px;top:126px;width:121px;height:42px;border-radius:21px;background:var(--band);color:#fff;font-size:13px;font-weight:400;display:flex;align-items:center;justify-content:center">Submit</div>
  <div class="brand" style="left:0;width:1200px;justify-content:center;top:215px;color:#fff"><span class="dot"></span>Brightwater Systems</div>
  <div class="abs" style="left:134px;top:300px;width:930px;height:1px;background:rgba(255,255,255,.18)"></div>
  <div class="abs" style="left:134px;top:360px;width:930px;height:1px;background:rgba(255,255,255,.12)"></div>
  <div class="abs" style="left:134px;top:371px;font-size:11px;color:#8b91a8">COPYRIGHT © 2021 BRIGHTWATER SYSTEMS</div>
  <div class="abs" style="left:842px;top:371px;width:222px;text-align:right;font-size:11px;color:#8b91a8">PRIVACY POLICY | TERMS OF SERVICES</div>
</footer>
<nav class="fnav">
  <a style="left:359px">HOME</a>
  <a class="active" style="left:465px">ABOUT US</a>
  <a style="left:594px">OUR SERVICES</a>
  <a style="left:710px">BLOG</a>
  <a style="left:821px">CONTACT US</a>
</nav>

</body>
</html>
```